Building Defect timeline illustration

We need an memorable illustration using iconography to plot the time frame for a building defects process. These are typically shown in single line format and not catchy. Designed to stand out. Powerpoint of the timeline attached. Colour blue to be dominant please.Can use building/construction imagery/icons.

Target Market(s)

Builders/Developers/General public

Industry/Entity Type

Property

Font styles to use
Sans Serif

Colors
0355a3
3176b5
ffffff

Requirements
Must have
• Visual appeal, ability to stick to the factual timeline.
Nice to have
• You could incorporate building/construction into the graphics- suggestion only.

```html
<!DOCTYPE html>
<html lang="en">
<head>
<meta charset="utf-8">
<title>Project Timeline – Building Defects Bond</title>
<link rel="stylesheet" href="https://fonts.googleapis.com/css2?family=Roboto+Condensed:wght@400;500&family=Roboto:wght@400&display=swap">
<style>
  :root {
    --blue-deep: #0355a3;
    --blue-mid: #3176b5;
    --white: #ffffff;
    --ink: #3a3a3a;
    --title-ink: #2e2e2e;
    --sky-top: #e9ebec;
    --sky-bottom: #f6f6f6;
    --skyline: #d6d9dc;
  }
  html, body {
    margin: 0;
    padding: 0;
    width: 1200px;
    height: 824px;
    overflow: hidden;
    background: var(--white);
  }
  .timeline-board {
    display: block;
    width: 1200px;
    height: 824px;
  }
  .board-title {
    font-family: "Roboto Condensed", "Arial Narrow", sans-serif;
    font-size: 40px;
    font-weight: 500;
    fill: var(--title-ink);
  }
  .title-rule { stroke: var(--blue-deep); stroke-width: 2.5; }
  .axis-band { fill: var(--white); }
  .axis-line { stroke: var(--blue-deep); stroke-width: 3; }
  .milestone-dot { fill: var(--blue-deep); stroke: var(--white); stroke-width: 1.5; }
  .milestone-badge { fill: var(--blue-mid); stroke: var(--white); stroke-width: 2.5; }
  .badge-icon { fill: none; stroke: var(--white); stroke-width: 2; stroke-linecap: round; stroke-linejoin: round; }
  .badge-icon-fill { fill: var(--white); }
  .leader { stroke: var(--blue-mid); stroke-width: 1.3; fill: none; }
  .milestone-label {
    font-family: "Roboto Condensed", "Arial Narrow", sans-serif;
    font-size: 10px;
    font-weight: 500;
    fill: var(--ink);
    text-anchor: middle;
  }
  .milestone-when {
    font-family: "Roboto", Arial, sans-serif;
    font-size: 10px;
    fill: var(--ink);
    text-anchor: middle;
  }
</style>
</head>
<body>
<svg class="timeline-board" viewBox="0 0 891 612" xmlns="http://www.w3.org/2000/svg">
  <defs>
    <linearGradient id="sky-wash" x1="0" y1="0" x2="0" y2="1">
      <stop offset="0" stop-color="var(--sky-top)"/>
      <stop offset="0.65" stop-color="var(--sky-top)"/>
      <stop offset="1" stop-color="var(--sky-bottom)"/>
    </linearGradient>
    <linearGradient id="skyline-wash" x1="0" y1="0" x2="0" y2="1">
      <stop offset="0" stop-color="var(--skyline)" stop-opacity="0"/>
      <stop offset="0.4" stop-color="var(--skyline)" stop-opacity="0.8"/>
      <stop offset="1" stop-color="var(--skyline)" stop-opacity="0.9"/>
    </linearGradient>
  </defs>

  <rect class="backdrop" x="0" y="0" width="891" height="612" fill="url(#sky-wash)"/>
  <rect class="skyline-area" role="img" aria-label="Faint grey city skyline silhouette behind the timeline"
        x="0" y="250" width="891" height="158" fill="url(#skyline-wash)"/>

  <text class="board-title" x="62" y="72" textLength="243" lengthAdjust="spacingAndGlyphs">PROJECT TIMELINE</text>
  <line class="title-rule" x1="325" y1="69" x2="891" y2="69"/>

  <rect class="axis-band" x="90" y="383" width="700" height="18"/>
  <line class="axis-line" x1="45" y1="392" x2="840" y2="392"/>

  <path class="leader" d="M102 392 V432 M92 432 H112"/>
  <path class="leader" d="M428 392 V492 M414 492 H442"/>
  <path class="leader" d="M517 392 V432 M507 432 H527"/>
  <path class="leader" d="M598 392 V492 M584 492 H612"/>
  <path class="leader" d="M700 392 V432 M690 432 H710"/>
  <path class="leader" d="M775 392 V492 M761 492 H789"/>
  <path class="leader" d="M102 291 V392 M428 353 V392 M517 290 V392 M598 353 V392 M700 290 V392 M775 353 V392"/>

  <g class="milestone-dots">
    <circle class="milestone-dot" cx="102" cy="392" r="5"/>
    <circle class="milestone-dot" cx="428" cy="392" r="5"/>
    <circle class="milestone-dot" cx="517" cy="392" r="5"/>
    <circle class="milestone-dot" cx="598" cy="392" r="5"/>
    <circle class="milestone-dot" cx="700" cy="392" r="5"/>
    <circle class="milestone-dot" cx="775" cy="392" r="5"/>
  </g>

  <g class="milestone milestone--bond">
    <text class="milestone-label"><tspan x="102" y="203">LODGE</tspan><tspan x="102" y="215">2% BOND</tspan></text>
    <circle class="milestone-badge" cx="102" cy="256" r="35"/>
    <g class="badge-icon">
      <rect x="82" y="240" width="40" height="28" rx="2"/>
      <circle cx="102" cy="250" r="6"/>
      <path d="M98 256 L96 274 L102 270 L108 274 L106 256"/>
    </g>
    <text class="milestone-when"><tspan x="102" y="450">Any time before</tspan><tspan x="102" y="463">OC issued</tspan></text>
  </g>

  <g class="milestone milestone--appoint">
    <text class="milestone-label"><tspan x="428" y="241">DEVELOPER</tspan><tspan x="428" y="253">TO APPOINT</tspan><tspan x="428" y="265">BUILDING INSPECTOR</tspan></text>
    <circle class="milestone-badge" cx="428" cy="318" r="35"/>
    <g class="badge-icon">
      <rect x="405" y="303" width="34" height="23" rx="2"/>
      <path d="M416 332 H428 M422 326 V332"/>
      <path d="M410 320 L417 313 L423 318 L434 308"/>
      <circle cx="444" cy="316" r="5"/>
      <path d="M436 334 Q444 322 452 334"/>
    </g>
    <text class="milestone-when"><tspan x="428" y="514">Within 12 months of</tspan><tspan x="428" y="527">completion</tspan><tspan x="428" y="540">of building work*</tspan></text>
  </g>

  <g class="milestone milestone--interim">
    <text class="milestone-label"><tspan x="517" y="198">INTERIM REPORT</tspan><tspan x="517" y="210">TO BE PROVIDED</tspan></text>
    <circle class="milestone-badge" cx="517" cy="255" r="35"/>
    <g class="badge-icon">
      <rect x="502" y="236" width="28" height="38" rx="2"/>
      <path d="M511 233 H521 V239 H511 Z"/>
      <path d="M508 246 H524 M508 252 H524"/>
      <path d="M500 264 Q516 252 532 264 Q516 276 500 264 Z"/>
      <circle cx="516" cy="264" r="4"/>
      <path d="M536 240 V270"/>
    </g>
    <text class="milestone-when"><tspan x="517" y="450">Within 15 – 18 months</tspan><tspan x="517" y="463">of completion of</tspan><tspan x="517" y="476">building work</tspan></text>
  </g>

  <g class="milestone milestone--inspection">
    <text class="milestone-label"><tspan x="598" y="224">DEVELOPER TO</tspan><tspan x="598" y="236">ARRANGE BUILDING</tspan><tspan x="598" y="248">INSPECTOR TO</tspan><tspan x="598" y="260">CARRY OUT FINAL</tspan><tspan x="598" y="272">INSPECTION</tspan></text>
    <circle class="milestone-badge" cx="598" cy="318" r="35"/>
    <g class="badge-icon">
      <rect x="580" y="298" width="26" height="34" rx="2"/>
      <path d="M584 305 l2 2 l3 -4 M592 305 H602 M584 314 l2 2 l3 -4 M592 314 H602 M584 323 l2 2 l3 -4 M592 323 H602"/>
      <circle cx="612" cy="322" r="5"/>
      <path d="M603 338 Q612 327 621 338"/>
    </g>
    <text class="milestone-when"><tspan x="598" y="514">Within 18 months of</tspan><tspan x="598" y="527">completion of</tspan><tspan x="598" y="540">building work</tspan></text>
  </g>

  <g class="milestone milestone--final">
    <text class="milestone-label"><tspan x="700" y="198">FINAL REPORT</tspan><tspan x="700" y="210">TO BE PROVIDED</tspan></text>
    <circle class="milestone-badge" cx="700" cy="255" r="35"/>
    <g class="badge-icon">
      <rect x="680" y="236" width="28" height="36" rx="1"/>
      <path d="M685 244 H703 M685 250 H703 M685 256 H697 M685 262 H697"/>
      <rect x="700" y="252" width="18" height="24" rx="2"/>
      <path d="M704 257 H714"/>
      <path d="M704 263 h2 M709 263 h2 M714 263 h0.5 M704 268 h2 M709 268 h2 M714 268 h0.5 M704 272 h2 M709 272 h2"/>
    </g>
    <text class="milestone-when"><tspan x="700" y="450">21 to 24 months</tspan><tspan x="700" y="463">after completion</tspan><tspan x="700" y="476">of building work</tspan></text>
  </g>

  <g class="milestone milestone--claim">
    <text class="milestone-label"><tspan x="775" y="241">LAST DATE FOR</tspan><tspan x="775" y="253">CLAIMING</tspan><tspan x="775" y="265">ON BOND</tspan></text>
    <circle class="milestone-badge" cx="775" cy="318" r="35"/>
    <g class="badge-icon">
      <rect x="755" y="302" width="40" height="34" rx="3"/>
      <path d="M755 312 H795 M764 298 V306 M786 298 V306"/>
    </g>
    <g class="badge-icon-fill">
      <rect x="760" y="317" width="4" height="3"/><rect x="767" y="317" width="4" height="3"/><rect x="774" y="317" width="4" height="3"/><rect x="781" y="317" width="4" height="3"/><rect x="788" y="317" width="4" height="3"/>
      <rect x="760" y="323" width="4" height="3"/><rect x="767" y="323" width="4" height="3"/><rect x="774" y="323" width="4" height="3"/><rect x="781" y="323" width="4" height="3"/><rect x="788" y="323" width="4" height="3"/>
      <rect x="760" y="329" width="4" height="3"/><rect x="767" y="329" width="4" height="3"/><rect x="774" y="329" width="4" height="3"/><rect x="781" y="329" width="4" height="3"/>
    </g>
    <text class="milestone-when"><tspan x="775" y="514">2 years after completion of</tspan><tspan x="775" y="527">work within 60 days of date</tspan><tspan x="775" y="540">of final inspection report</tspan><tspan x="775" y="553">(whichever is the later)</tspan></text>
  </g>
</svg>
</body>
</html>
```